Package Design for 15 lines of Tea

I need design variations for 15 different Tea lines.
The tea will be packaged in Tin cylinders.
I have attached several pictures to show you an example of the display we are modelling after along with other references.
The 15 tea lines are:
Study Tea
Ingredients: Brazilian Mate, Mint
Energy Boost Tea
Ingredients: Yunnan Coffee, Dark Puer
Relaxation Tea
Ingredients: Lotus Flower, South African Rooibos
Beauty Tea
Ingredients: Rose, Chrysanthemum, Red Dates, Huangqi
Sore Throat Tea
Ingredients: Honeysuckle, Pang Da Hai, Chamomile, Licorice Root
Get Well Tea
Ingredients: Ginger, Rooibos, Orange peel, Chinese Angelica
Diet Tea
Ingredients: Puer, Hibiscus, Lemongrass, Lotus Plumule
Bedtime Tea
Ingredients: Apple, Orange, Chamomile
South African Rooibos Tea
(pure)
Brazilian Yerba Mate Tea
(pure)
Long Jing Green Tea
(pure)
Darjeeling Black Tea
(pure)
Nepal Golden Tea
(Pure)
Bai Mu Dan White Tea
(pure)
Phoenix Oolong Tea
(pure)
Every Tea Blend should have three unique symbols that describe the purpose and theme of the blend. (!!Please don't make specific reference to the ingredients of the blends because some of these ingredients may be changed later. Stick to focusing on the intended purpose of the tea blend!!)
I would like the symbols to keep the same brushlike style that is consistent with our company logo.
Please keep the three block structure. I suggest keeping to just one color per tea blend. This will help each blend stand out between one another. I have a sample of the "Diet Tea" attached that I did myself to give you an idea of the structure I'm looking for, but obviously it's just my amateur version. Hope you can make them look far more appealing.
The ultimate goal is to build a picture language unique to our brand. As more products are released, we intend to potentially have hundreds of symbols, each with it's own meaning. So it would be nice when you present your pictures if you explain its intended meaning or message.
Deminsions:
Cylinder type 1: 82mm*38mmH
circular labels (along with your design) will be placed on the cap of product, and then the cylinder will be slanted on it's side to display the cap towards the customer.
Cylinder type 2: 65mm*152mmH
the labels will be placed on the side of the cylinder. In this version, try lining the three symbols in a vertical position. If this looks awful to you then feel free to go back to the horizontal style, but it would be nice to see what the vertical version looks like for reference.
Updates
Due to the scope of this project, please take note that I just increased my budget an additional 500 dollars more.
I also just added a 100 dollar second place prize. Don't want to see hard work unrewarded.
Feel free to send a few samples and I will provide prompt feedback. Please don't feel that you must submit all 15 lines at the same time.
Project Deadline Extended
Reason: I am extending the deadline as I feel there are more detailed revisions that need to be made until final selection.
Target Market(s)
Middle to Upper Class Consumers in China
Industry/Entity Type
It Company
Other font styles liked:
- font similar to font on company logo
Requirements
Must have
- Tea Designs must be in harmony with company logo and theme.
Should not have
- Avoid using Chinese characters as symbols. They may seem cool to westerners, but it's tacky for Chinese consumers.

```html
<!DOCTYPE html>
<html lang="en">
<head>
<meta charset="utf-8">
<title>Hollin Tea – Cap Label Range</title>
<link rel="stylesheet" href="https://fonts.googleapis.com/css2?family=Special+Elite&display=swap">
<style>
  :root {
    --page: #ffffff;
    --band: #0b0b0b;
    --ink: #1a1a1a;
    --glyph-blue: #56c2f0;
    --glyph-orange: #f39a1e;
    --glyph-yellow: #f2d21c;
    --sore-throat: #b5cf14;
    --get-well: #b995c6;
    --diet: #f3e600;
    --oolong: #d3cbc6;
    --white-tea: #ececec;
    --relaxation: #a6d29a;
    --beauty: #e07fae;
    --yerba-mate: #f8bf78;
    --golden: #e2c47a;
    --green-tea: #a3dcd5;
    --rooibos: #f19476;
    --energy: #f4920f;
    --study: #a2d7f2;
    --bedtime: #b3b6df;
    --black-tea: #a7c2dc;
  }
  * { margin: 0; padding: 0; box-sizing: border-box; }
  html, body { width: 1200px; height: 1000px; overflow: hidden; background: var(--page); }
  .range { position: relative; width: 1200px; height: 1000px; }
  .cap-label {
    position: absolute; width: 160px; height: 160px; margin: -80px 0 0 -80px;
    border-radius: 50%; overflow: hidden; background: var(--tone);
    font-family: "Special Elite", "Courier New", monospace; color: var(--ink);
  }
  .cap-label::after {
    content: ""; position: absolute; inset: 5px; border-radius: 50%;
    border: 1px solid rgba(255,255,255,.75);
  }
  .brand {
    position: absolute; top: 12px; left: 0; right: 0; text-align: center;
    font-size: 7px; line-height: 8px;
  }
  .brand-mark { display: block; width: 10px; height: 10px; margin: 2px auto 0; background: var(--band); }
  .tea-name {
    position: absolute; top: 36px; left: 14px; right: 14px; text-align: center;
    font-size: 13px; line-height: 14px; font-weight: 400;
  }
  .purpose-band {
    position: absolute; top: 72px; left: 0; right: 0; height: 24px; background: var(--band);
    display: flex; justify-content: center; align-items: center; gap: 16px;
  }
  .glyph { display: block; width: 16px; height: 16px; border-radius: 3px; }
  .glyph-blue { background: var(--glyph-blue); }
  .glyph-orange { background: var(--glyph-orange); }
  .glyph-yellow { background: var(--glyph-yellow); }
  .ingredients {
    position: absolute; top: 102px; left: 30px; right: 30px; text-align: center;
    font-size: 6px; line-height: 7px; text-transform: uppercase;
  }
</style>
</head>
<body>
<main class="range">
  <!-- Row 1 -->
  <section class="cap-label" style="left:145px;top:170px;--tone:var(--sore-throat)">
    <div class="brand">Hollin Tea<span class="brand-mark"></span></div>
    <h2 class="tea-name">Sore Throat<br>Tea</h2>
    <div class="purpose-band">
      <span class="glyph glyph-blue" role="img" aria-label="Brush-style pictogram: soothing"></span>
      <span class="glyph glyph-orange" role="img" aria-label="Brush-style pictogram: clear voice"></span>
      <span class="glyph glyph-yellow" role="img" aria-label="Brush-style pictogram: lightness"></span>
    </div>
    <p class="ingredients">Honeysuckle, Pang Da Hai, Chamomile, Licorice Root</p>
  </section>
  <section class="cap-label" style="left:372px;top:170px;--tone:var(--get-well)">
    <div class="brand">Hollin Tea<span class="brand-mark"></span></div>
    <h2 class="tea-name">Get Well<br>Tea</h2>
    <div class="purpose-band">
      <span class="glyph glyph-blue" role="img" aria-label="Brush-style pictogram: recovery"></span>
      <span class="glyph glyph-orange" role="img" aria-label="Brush-style pictogram: health"></span>
      <span class="glyph glyph-yellow" role="img" aria-label="Brush-style pictogram: care"></span>
    </div>
    <p class="ingredients">Ginger, Rooibos, Orange Peel, Chinese Angelica</p>
  </section>
  <section class="cap-label" style="left:602px;top:170px;--tone:var(--diet)">
    <div class="brand">Hollin Tea<span class="brand-mark"></span></div>
    <h2 class="tea-name">Diet<br>Tea</h2>
    <div class="purpose-band">
      <span class="glyph glyph-blue" role="img" aria-label="Brush-style pictogram: lightness"></span>
      <span class="glyph glyph-orange" role="img" aria-label="Brush-style pictogram: balance"></span>
      <span class="glyph glyph-yellow" role="img" aria-label="Brush-style pictogram: fresh"></span>
    </div>
    <p class="ingredients">Puer, Hibiscus, Lemongrass, Lotus Plumule</p>
  </section>
  <section class="cap-label" style="left:833px;top:170px;--tone:var(--oolong)">
    <div class="brand">Hollin Tea<span class="brand-mark"></span></div>
    <h2 class="tea-name">Phoenix<br>Oolong Tea</h2>
    <div class="purpose-band">
      <span class="glyph glyph-blue" role="img" aria-label="Brush-style pictogram: aroma"></span>
      <span class="glyph glyph-orange" role="img" aria-label="Brush-style pictogram: flavour"></span>
      <span class="glyph glyph-yellow" role="img" aria-label="Brush-style pictogram: pure leaf"></span>
    </div>
  </section>
  <section class="cap-label" style="left:1063px;top:170px;--tone:var(--white-tea)">
    <div class="brand">Hollin Tea<span class="brand-mark"></span></div>
    <h2 class="tea-name">Bai Mu Dan<br>White Tea</h2>
    <div class="purpose-band">
      <span class="glyph glyph-blue" role="img" aria-label="Brush-style pictogram: aroma"></span>
      <span class="glyph glyph-orange" role="img" aria-label="Brush-style pictogram: flavour"></span>
      <span class="glyph glyph-yellow" role="img" aria-label="Brush-style pictogram: pure leaf"></span>
    </div>
  </section>

  <!-- Row 2 -->
  <section class="cap-label" style="left:258px;top:320px;--tone:var(--relaxation)">
    <div class="brand">Hollin Tea<span class="brand-mark"></span></div>
    <h2 class="tea-name">Relaxation<br>Tea</h2>
    <div class="purpose-band">
      <span class="glyph glyph-blue" role="img" aria-label="Brush-style pictogram: ease"></span>
      <span class="glyph glyph-orange" role="img" aria-label="Brush-style pictogram: calm mind"></span>
      <span class="glyph glyph-yellow" role="img" aria-label="Brush-style pictogram: bloom"></span>
    </div>
    <p class="ingredients">Lotus Flower, South African Rooibos</p>
  </section>
  <section class="cap-label" style="left:487px;top:320px;--tone:var(--beauty)">
    <div class="brand">Hollin Tea<span class="brand-mark"></span></div>
    <h2 class="tea-name">Beauty<br>Tea</h2>
    <div class="purpose-band">
      <span class="glyph glyph-blue" role="img" aria-label="Brush-style pictogram: love"></span>
      <span class="glyph glyph-orange" role="img" aria-label="Brush-style pictogram: radiance"></span>
      <span class="glyph glyph-yellow" role="img" aria-label="Brush-style pictogram: glow"></span>
    </div>
    <p class="ingredients">Rose, Chrysanthemum, Red Dates, Huangqi</p>
  </section>
  <section class="cap-label" style="left:718px;top:320px;--tone:var(--yerba-mate)">
    <div class="brand">Hollin Tea<span class="brand-mark"></span></div>
    <h2 class="tea-name">Brazilian<br>Yerba Mate Tea</h2>
    <div class="purpose-band">
      <span class="glyph glyph-blue" role="img" aria-label="Brush-style pictogram: aroma"></span>
      <span class="glyph glyph-orange" role="img" aria-label="Brush-style pictogram: flavour"></span>
      <span class="glyph glyph-yellow" role="img" aria-label="Brush-style pictogram: pure leaf"></span>
    </div>
  </section>
  <section class="cap-label" style="left:948px;top:320px;--tone:var(--golden)">
    <div class="brand">Hollin Tea<span class="brand-mark"></span></div>
    <h2 class="tea-name">Nepal<br>Golden Tea</h2>
    <div class="purpose-band">
      <span class="glyph glyph-blue" role="img" aria-label="Brush-style pictogram: aroma"></span>
      <span class="glyph glyph-orange" role="img" aria-label="Brush-style pictogram: flavour"></span>
      <span class="glyph glyph-yellow" role="img" aria-label="Brush-style pictogram: pure leaf"></span>
    </div>
  </section>

  <!-- Row 3 -->
  <section class="cap-label" style="left:372px;top:470px;--tone:var(--green-tea)">
    <div class="brand">Hollin Tea<span class="brand-mark"></span></div>
    <h2 class="tea-name">Long Jing<br>Green Tea</h2>
    <div class="purpose-band">
      <span class="glyph glyph-blue" role="img" aria-label="Brush-style pictogram: aroma"></span>
      <span class="glyph glyph-orange" role="img" aria-label="Brush-style pictogram: flavour"></span>
      <span class="glyph glyph-yellow" role="img" aria-label="Brush-style pictogram: pure leaf"></span>
    </div>
  </section>
  <section class="cap-label" style="left:602px;top:470px;--tone:var(--rooibos)">
    <div class="brand">Hollin Tea<span class="brand-mark"></span></div>
    <h2 class="tea-name">South African<br>Rooibos Tea</h2>
    <div class="purpose-band">
      <span class="glyph glyph-blue" role="img" aria-label="Brush-style pictogram: vitality"></span>
      <span class="glyph glyph-orange" role="img" aria-label="Brush-style pictogram: origin"></span>
      <span class="glyph glyph-yellow" role="img" aria-label="Brush-style pictogram: sweetness"></span>
    </div>
  </section>
  <section class="cap-label" style="left:833px;top:470px;--tone:var(--energy)">
    <div class="brand">Hollin Tea<span class="brand-mark"></span></div>
    <h2 class="tea-name">Energy Boost<br>Tea</h2>
    <div class="purpose-band">
      <span class="glyph glyph-blue" role="img" aria-label="Brush-style pictogram: daylight"></span>
      <span class="glyph glyph-orange" role="img" aria-label="Brush-style pictogram: power"></span>
      <span class="glyph glyph-yellow" role="img" aria-label="Brush-style pictogram: recharge"></span>
    </div>
    <p class="ingredients">Yunnan Coffee, Dark Puer</p>
  </section>

  <!-- Row 4 -->
  <section class="cap-label" style="left:487px;top:620px;--tone:var(--study)">
    <div class="brand">Hollin Tea<span class="brand-mark"></span></div>
    <h2 class="tea-name">Study<br>Tea</h2>
    <div class="purpose-band">
      <span class="glyph glyph-blue" role="img" aria-label="Brush-style pictogram: ideas"></span>
      <span class="glyph glyph-orange" role="img" aria-label="Brush-style pictogram: learning"></span>
      <span class="glyph glyph-yellow" role="img" aria-label="Brush-style pictogram: focus"></span>
    </div>
    <p class="ingredients">Brazilian Mate, Mint</p>
  </section>
  <section class="cap-label" style="left:718px;top:620px;--tone:var(--bedtime)">
    <div class="brand">Hollin Tea<span class="brand-mark"></span></div>
    <h2 class="tea-name">Bedtime<br>Tea</h2>
    <div class="purpose-band">
      <span class="glyph glyph-blue" role="img" aria-label="Brush-style pictogram: rest"></span>
      <span class="glyph glyph-orange" role="img" aria-label="Brush-style pictogram: night"></span>
      <span class="glyph glyph-yellow" role="img" aria-label="Brush-style pictogram: sweet dreams"></span>
    </div>
    <p class="ingredients">Apple, Orange, Chamomile</p>
  </section>

  <!-- Row 5 -->
  <section class="cap-label" style="left:602px;top:770px;--tone:var(--black-tea)">
    <div class="brand">Hollin Tea<span class="brand-mark"></span></div>
    <h2 class="tea-name">Darjeeling<br>Black Tea</h2>
    <div class="purpose-band">
      <span class="glyph glyph-blue" role="img" aria-label="Brush-style pictogram: aroma"></span>
      <span class="glyph glyph-orange" role="img" aria-label="Brush-style pictogram: flavour"></span>
      <span class="glyph glyph-yellow" role="img" aria-label="Brush-style pictogram: pure leaf"></span>
    </div>
  </section>
</main>
</body>
</html>
```